Interior Design/ New Construction interior finishes

Interior Design Website

Target Market(s)

Home builders, New Construction, Renovations, Public

Industry/Entity Type

Construction

Coding

Coded - Design and coding required

Number of Pages Required

1 page

Font styles to use
Sans Serif

Colors

Designer to choose colors to be used in the design.

Requirements
Must have
• Section to upload pictures of projects
• Simple and modern design
• Designer 1 details about myself
• Logo
• Upload section for photos for future jobs
Nice to have
• Sections they can click on to see certain rooms in a house
• Decorating, floral arrangements, holiday decorating.
• I have lots of before and after as well. Maybe a section for those.

```html
<!DOCTYPE html>
<html lang="en">
<head>
<meta charset="utf-8">
<title>Lumen Designs — Interior Design</title>
<link href="https://fonts.googleapis.com/css2?family=Josefin+Sans:wght@300;400;600&family=Lato:wght@400;700;900&display=swap" rel="stylesheet">
<style>
:root{
  --ink:#111;
  --text:#333;
  --muted:#666;
  --soft:#f7f7f7;
  --white:#fff;
  --dark-card:#575757;
  --footer:#1b1b1b;
  --line:#222;
}
*{box-sizing:border-box;margin:0;padding:0}
html,body{width:1200px;height:4265px;overflow:hidden}
body{font-family:'Lato',sans-serif;color:var(--text);background:var(--white);position:relative}
section,header,footer{position:absolute;left:0;width:1200px}
.abs{position:absolute}
.title{font-family:'Josefin Sans',sans-serif;font-weight:300;font-size:27px;color:var(--ink);text-align:center;width:100%;letter-spacing:1px}
.btn{position:absolute;height:32px;border:2px solid var(--ink);border-radius:16px;font-family:'Lato',sans-serif;font-size:13px;letter-spacing:1px;color:var(--ink);display:flex;align-items:center;justify-content:center;background:var(--white)}

/* hero */
.hero{top:0;height:625px;background:linear-gradient(180deg,#8a8f98 0%,#a9a295 35%,#8c7a64 60%,#4e7fa0 82%,#6b8f4a 100%)}
.brand{position:absolute;top:30px;left:0;width:100%;text-align:center;color:var(--white);font-family:'Josefin Sans',sans-serif;font-size:20px;letter-spacing:2px}
.brand .mark{display:block;margin:0 auto 6px;width:46px;height:46px;border:2px solid var(--white);border-radius:50%}
.menu{position:absolute;top:62px;right:50px;width:26px}
.menu span{display:block;height:3px;background:var(--white);margin-bottom:5px}
.hero-tag{position:absolute;top:292px;width:100%;text-align:center;color:var(--white);font-family:'Josefin Sans',sans-serif;font-size:30px;letter-spacing:5px}
.hero .btn{left:530px;top:337px;width:140px;background:transparent;border-color:var(--white);color:var(--white)}

/* about */
.about{top:625px;height:527px;background:var(--soft)}
.about-frame{left:199px;top:92px;width:302px;height:380px;border:2px solid var(--ink)}
.about-photo{left:216px;top:85px;width:285px;height:375px;background:linear-gradient(160deg,#d9d7d2,#a8a49c 55%,#4a4642)}
.h-caps{font-family:'Josefin Sans',sans-serif;font-size:27px;letter-spacing:4px;color:var(--ink)}
.about-text{left:532px;top:93px;width:380px;font-size:14px;line-height:1.4}
.about-text p{margin-top:10px}
.read{font-size:13px;margin-top:6px;display:block}
.services{left:532px;top:238px}
.svc-row{display:flex;gap:50px;margin-top:26px}
.svc{text-align:center;width:80px;font-size:12px;letter-spacing:1px;color:var(--ink)}
.svc .ico{width:60px;height:60px;border:2px solid var(--ink);border-radius:50%;margin:0 auto 10px;display:flex;align-items:center;justify-content:center}
.about .btn{left:534px;top:420px;width:140px}

/* work */
.work{top:1152px;height:540px}
.work .title{top:73px;position:absolute}
.video-frame{left:378px;top:165px;width:497px;height:322px;border:2px solid var(--ink)}
.video{left:352px;top:136px;width:502px;height:324px;background:linear-gradient(120deg,#7d8fa0,#e6e8ec 45%,#c4c8cf 70%,#8d7c7b)}
.play{left:573px;top:268px}

/* team */
.team{top:1692px;height:616px;background:var(--soft)}
.team .title{position:absolute;top:85px}
.member{position:absolute;top:253px;width:210px;height:281px;background:var(--white);border-radius:16px;text-align:center;padding-top:85px}
.member.active{background:var(--dark-card);color:var(--white)}
.avatar{position:absolute;top:-75px;left:39px;width:132px;height:132px;border-radius:50%;border:4px solid var(--white);background:linear-gradient(180deg,#9a9590,#3d3a38)}
.member h3{font-size:17px;font-weight:900;color:inherit;line-height:1.2}
.member h4{font-size:16px;font-weight:700;line-height:1.2;margin-bottom:12px}
.member p{font-size:13px;line-height:1.35;padding:0 22px}
.member:not(.active) h3,.member:not(.active) h4{color:var(--ink)}
.share{position:absolute;right:20px;bottom:16px}

/* projects */
.projects{top:2308px;height:543px}
.projects .title{position:absolute;top:72px}
.strip{position:absolute;top:143px;left:0;width:1200px;height:241px;display:flex}
.strip div{flex:1;height:100%}
.strip .p1{background:linear-gradient(160deg,#7a5a3c,#c9b69d)}
.strip .p2{background:linear-gradient(160deg,#4b3a35,#8a2a2a);border:4px solid var(--ink);position:relative;display:flex;align-items:center;justify-content:center}
.strip .p3{background:linear-gradient(160deg,#e8e6e3,#bfbcb8)}
.strip .p4{background:linear-gradient(160deg,#3a3a3a,#d5d5d5)}
.strip .p5{background:linear-gradient(160deg,#5c3d24,#b58b62)}
.projects .btn{left:534px;top:458px;width:140px}

/* blogs */
.blogs{top:2851px;height:723px;background:var(--soft)}
.blogs .title{position:absolute;top:70px}
.post{position:absolute;top:129px;width:310px;height:440px;background:var(--white);padding:0 0 0}
.post.active{background:#000;color:var(--white)}
.post-img{height:238px;margin:0 0 0 0;background:linear-gradient(170deg,#e9e7e3,#a9a59e 60%,#59554f)}
.post.active .post-img{margin:6px 6px 0;height:232px}
.post-body{padding:14px 16px}
.meta{font-size:11px;line-height:1.4}
.post h3{font-size:17px;font-weight:900;margin:6px 0 10px;color:inherit}
.post:not(.active) h3{color:var(--ink)}
.post p{font-size:13px;line-height:1.4}
.post .read{margin-top:6px}
.dots{position:absolute;top:3460px}
.dot-row{position:absolute;top:608px;left:575px;display:flex;gap:6px}
.dot-row i{width:8px;height:8px;border-radius:50%;background:#bbb;display:block}
.dot-row i:first-child{background:var(--ink)}
.blogs .btn{left:534px;top:640px;width:140px}

/* newsletter */
.news{top:3574px;height:258px}
.news .title{position:absolute;top:75px;font-size:25px}
.subscribe{position:absolute;left:335px;top:128px;width:532px;height:44px;border:2px solid #bbb;border-radius:22px;display:flex;align-items:center;padding-left:30px;font-size:13px;color:#999}
.subscribe .send{position:absolute;right:-2px;top:-2px;width:98px;height:44px;background:var(--ink);border-radius:22px;display:flex;align-items:center;justify-content:center}

/* footer */
.footer{top:3832px;height:433px;background:linear-gradient(180deg,#2a2a2a,#141414);color:var(--white)}
.f-col{position:absolute;top:50px;font-size:15px;line-height:1.4}
.f-col strong{font-size:17px;font-weight:700;display:block;margin-bottom:4px}
.f-div{position:absolute;top:50px;width:3px;height:70px;background:var(--white)}
.f-rule{position:absolute;left:122px;width:960px;height:2px;background:var(--white)}
.f-brand{position:absolute;left:120px;top:170px;width:230px;font-size:13px;line-height:1.4}
.f-brand .name{font-family:'Josefin Sans',sans-serif;font-size:18px;letter-spacing:2px;display:flex;align-items:center;gap:10px;margin-bottom:12px}
.f-brand .mark{width:36px;height:36px;border:2px solid var(--white);border-radius:50%}
.f-links{position:absolute;left:455px;top:170px}
.f-links h5,.f-sub h5{font-size:17px;font-weight:700;margin-bottom:12px}
.f-links li{list-style:none;font-size:11px;line-height:22px;letter-spacing:.5px}
.f-sub{position:absolute;left:790px;top:170px}
.f-sub .field{width:290px;height:30px;background:var(--white);display:flex;align-items:center;padding-left:10px;font-size:13px;color:var(--ink);position:relative}
.f-sub .field span{position:absolute;right:0;top:0;width:40px;height:30px;background:var(--ink);border:2px solid var(--white);display:flex;align-items:center;justify-content:center}
.copy{position:absolute;left:122px;top:392px;font-size:13px}
.social{position:absolute;right:120px;top:384px;display:flex;gap:8px}
.social i{display:block;width:28px;height:28px;border:2px solid var(--white);border-radius:50%}
</style>
</head>
<body>

<header class="hero" role="img" aria-label="Photo of a brick family home with a pool and garden at dusk">
  <div class="brand"><span class="mark"></span>Lumen Designs</div>
  <div class="menu"><span></span><span></span><span></span></div>
  <h1 class="hero-tag">LET YOUR HOME STYLISH</h1>
  <a class="btn">READ MORE</a>
</header>

<section class="about">
  <div class="abs about-frame"></div>
  <div class="abs about-photo" role="img" aria-label="Photo of a dining room with a chandelier, white chairs and flowers"></div>
  <div class="abs about-text">
    <h2 class="h-caps">ABOUT US</h2>
    <p>Lorem Ipsum is simply dummy text of the printing and typesetting industry.</p>
    <span class="read">Read More....</span>
  </div>
  <div class="abs services">
    <h2 class="h-caps">OUR SERVICES</h2>
    <div class="svc-row">
      <div class="svc"><div class="ico"><svg width="26" height="26" viewBox="0 0 24 24" fill="none" stroke="#111" stroke-width="1.8"><path d="M3 11l9-7 9 7v9H3z"/><path d="M9 20v-6h6v6"/></svg></div>INTERIOR</div>
      <div class="svc"><div class="ico"><svg width="26" height="26" viewBox="0 0 24 24" fill="none" stroke="#111" stroke-width="1.8"><rect x="4" y="4" width="16" height="16"/><circle cx="12" cy="12" r="4"/></svg></div>DESIGNING</div>
      <div class="svc"><div class="ico"><svg width="26" height="26" viewBox="0 0 24 24" fill="none" stroke="#111" stroke-width="1.8"><path d="M9 17h6M10 21h4M12 3a6 6 0 0 0-4 10.5c.8.8 1 1.5 1 2.5h6c0-1 .2-1.7 1-2.5A6 6 0 0 0 12 3z"/></svg></div>IDEAS</div>
    </div>
  </div>
  <a class="btn">VIEW MORE</a>
</section>

<section class="work">
  <h2 class="title">How We Work</h2>
  <div class="abs video-frame"></div>
  <div class="abs video" role="img" aria-label="Video still of workers finishing a textured feature wall"></div>
  <svg class="abs play" width="62" height="62" viewBox="0 0 62 62"><circle cx="31" cy="31" r="29" fill="rgba(255,255,255,.35)" stroke="#fff" stroke-width="2"/><path d="M25 19l18 12-18 12z" fill="#fff"/></svg>
</section>

<section class="team">
  <h2 class="title">Meet Our Team</h2>
  <div class="member active" style="left:125px">
    <div class="avatar" role="img" aria-label="Portrait of Daniel"></div>
    <h3>Daniel</h3><h4>Senior Interior<br>Designer</h4>
    <p>Lorem Ipsum is simply dummy text of the printing and typesetting industry.</p>
    <svg class="share" width="18" height="18" viewBox="0 0 24 24" fill="#fff"><circle cx="18" cy="5" r="3"/><circle cx="6" cy="12" r="3"/><circle cx="18" cy="19" r="3"/><path d="M8 11l8-5M8 13l8 5" stroke="#fff" stroke-width="2"/></svg>
  </div>
  <div class="member" style="left:372px">
    <div class="avatar" role="img" aria-label="Portrait of Fernando"></div>
    <h3>Fernando</h3><h4>Workspace<br>Analyst</h4>
    <p>Lorem Ipsum is simply dummy text of the printing and typesetting industry.</p>
    <svg class="share" width="18" height="18" viewBox="0 0 24 24" fill="#111"><circle cx="18" cy="5" r="3"/><circle cx="6" cy="12" r="3"/><circle cx="18" cy="19" r="3"/><path d="M8 11l8-5M8 13l8 5" stroke="#111" stroke-width="2"/></svg>
  </div>
  <div class="member" style="left:620px">
    <div class="avatar" role="img" aria-label="Portrait of Jonah"></div>
    <h3>Jonah</h3><h4>Project<br>Manager</h4>
    <p>Lorem Ipsum is simply dummy text of the printing and typesetting industry.</p>
    <svg class="share" width="18" height="18" viewBox="0 0 24 24" fill="#111"><circle cx="18" cy="5" r="3"/><circle cx="6" cy="12" r="3"/><circle cx="18" cy="19" r="3"/><path d="M8 11l8-5M8 13l8 5" stroke="#111" stroke-width="2"/></svg>
  </div>
  <div class="member" style="left:868px">
    <div class="avatar" role="img" aria-label="Portrait of Marissa"></div>
    <h3>Marissa</h3><h4>Junior Interior<br>Designer</h4>
    <p>Lorem Ipsum is simply dummy text of the printing and typesetting industry.</p>
    <svg class="share" width="18" height="18" viewBox="0 0 24 24" fill="#111"><circle cx="18" cy="5" r="3"/><circle cx="6" cy="12" r="3"/><circle cx="18" cy="19" r="3"/><path d="M8 11l8-5M8 13l8 5" stroke="#111" stroke-width="2"/></svg>
  </div>
</section>

<section class="projects">
  <h2 class="title">Projects</h2>
  <div class="strip">
    <div class="p1" role="img" aria-label="Project photo: wood-beamed dining room"></div>
    <div class="p2" role="img" aria-label="Project photo: home theater with red carpet">
      <svg width="42" height="42" viewBox="0 0 24 24" fill="none" stroke="#fff" stroke-width="1.6"><circle cx="10" cy="10" r="6"/><path d="M14.5 14.5L20 20M10 7v6M7 10h6"/></svg>
    </div>
    <div class="p3" role="img" aria-label="Project photo: white bathroom with freestanding tub"></div>
    <div class="p4" role="img" aria-label="Project photo: modern kitchen with black fixtures"></div>
    <div class="p5" role="img" aria-label="Project photo: warm living room with fireplace"></div>
  </div>
  <a class="btn">VIEW MORE</a>
</section>

<section class="blogs">
  <h2 class="title">Blogs</h2>
  <article class="post active" style="left:122px">
    <div class="post-img" role="img" aria-label="Blog photo: dining room with white chairs"></div>
    <div class="post-body"><div class="meta">Feb.19,2018<br>By&nbsp; PETER LANE</div>
      <h3>LOREAM IPSUM</h3>
      <p>Lorem Ipsum is simply dummy text of the printing and typesetting industry. Lorem Ipsum has been the industry's standard dummy text.</p>
      <span class="read">Read More....</span></div>
  </article>
  <article class="post" style="left:449px">
    <div class="post-img" role="img" aria-label="Blog photo: rustic dining table"></div>
    <div class="post-body"><div class="meta">Feb.19,2018<br>By&nbsp; PETER LANE</div>
      <h3>LOREAM IPSUM</h3>
      <p>Lorem Ipsum is simply dummy text of the printing and typesetting industry. Lorem Ipsum has been the industry's standard dummy text.</p>
      <span class="read">Read More....</span></div>
  </article>
  <article class="post" style="left:773px">
    <div class="post-img" role="img" aria-label="Blog photo: bright living room with flowers"></div>
    <div class="post-body"><div class="meta">Feb.19,2018<br>By&nbsp; PETER LANE</div>
      <h3>LOREAM IPSUM</h3>
      <p>Lorem Ipsum is simply dummy text of the printing and typesetting industry. Lorem Ipsum has been the industry's standard dummy text.</p>
      <span class="read">Read More....</span></div>
  </article>
  <div class="dot-row"><i></i><i></i><i></i></div>
  <a class="btn">VIEW MORE</a>
</section>

<section class="news">
  <h2 class="title">Subscribe For Our Newsletter</h2>
  <div class="subscribe">Your E-mail Here
    <span class="send"><svg width="22" height="22" viewBox="0 0 24 24" fill="#fff"><path d="M2 11l20-8-7 19-3-8z"/></svg></span>
  </div>
</section>

<footer class="footer">
  <div class="f-col" style="left:122px"><strong>Call Us Now</strong>202-555-0147</div>
  <div class="f-div" style="left:385px"></div>
  <div class="f-col" style="left:517px"><strong>Come Visit Us</strong>48 Harbor Ln. Coral Bay,<br>FL 32911</div>
  <div class="f-div" style="left:815px"></div>
  <div class="f-col" style="left:922px;text-align:right;width:158px"><strong>Send Massage</strong>hello@lumendesigns.com</div>
  <div class="f-rule" style="top:143px"></div>
  <div class="f-brand">
    <div class="name"><span class="mark"></span>Lumen Designs</div>
    Lorem Ipsum is simply dummy text of the printing and typesetting industry.
    <span class="read">Read More....</span>
  </div>
  <div class="f-links"><h5>Quick Link</h5>
    <ul><li>HOME</li><li>ABOUT</li><li>SERVICES</li><li>PROJECTS</li><li>BLOGS</li><li>CONTACT</li></ul>
  </div>
  <div class="f-sub"><h5>Subscribe Now</h5>
    <div class="field">E-Mail<span><svg width="16" height="16" viewBox="0 0 24 24" fill="#fff"><path d="M2 11l20-8-7 19-3-8z"/></svg></span></div>
  </div>
  <div class="f-rule" style="top:376px"></div>
  <div class="copy">CopyRight © 2018 LumenDesigns. All Right Reserve</div>
  <div class="social"><i></i><i></i><i></i></div>
</footer>

</body>
</html>
```